BEACON CABS

Taxi card design

Need changes very slow in replying to my messages.

Target Market(s)

Customers

Industry/Entity Type

Taxi

Contact Information for Business Card

See previous design

Font styles to use
Sans Serif

Colors
A7469A
B969AE
D3A5CF
EDDBEB
F8F0F9
6B429C
8869AF
B7A5CE
E3DAEB
F3F0F8

Requirements
Nice to have
• We are in the business of looking after people, not just driving vehicles front
Should not have
• Front number 01632 480 480 needs to big big

```html
<!DOCTYPE html>
<html lang="en">
<head>
<meta charset="utf-8">
<title>Beacon Cabs – Business Card</title>
<link href="https://fonts.googleapis.com/css2?family=Montserrat:wght@600;700&family=Poppins:wght@400;600;700&display=swap" rel="stylesheet">
<style>
  :root{
    --magenta:#a7469a;
    --magenta-deep:#a2378f;
    --violet:#6b429c;
    --violet-deep:#66308a;
    --ink:#111111;
    --paper:#ffffff;
    --backdrop:#ece8ee;
    --grad:linear-gradient(135deg,var(--magenta-deep) 0%,var(--violet-deep) 100%);
  }
  *{box-sizing:border-box;margin:0;padding:0}
  html,body{width:1189px;height:1200px;overflow:hidden}
  body{background:var(--backdrop);position:relative;font-family:"Poppins",sans-serif}

  .card{position:absolute;left:169px;width:852px;height:487px;overflow:hidden;box-shadow:0 4px 14px rgba(0,0,0,.18)}
  .card--info{top:111px;background:var(--paper)}
  .card--front{top:640px;background:var(--grad)}

  /* info side */
  .brand{position:absolute;left:32px;top:78px;display:flex;align-items:center;gap:12px;
    font-family:"Montserrat",sans-serif;font-weight:700;font-size:45px;line-height:54px;letter-spacing:-.5px;color:var(--magenta);white-space:nowrap}
  .brand__mark{width:20px;height:20px;background:var(--violet);flex:none}

  .line-list{position:absolute;left:62px;top:185px;display:flex;flex-direction:column;gap:27px}
  .line{width:312px;height:51px;border-radius:14px 4px 4px 14px;background:var(--grad);
    display:flex;align-items:center;padding-left:12px;gap:9px;
    font-family:"Montserrat",sans-serif;font-weight:600;font-size:27px;letter-spacing:2.5px;color:var(--paper);white-space:nowrap}
  .line__icon{width:30px;height:30px;border-radius:6px;background:var(--paper);display:flex;align-items:center;justify-content:center;flex:none}
  .line__icon svg{width:20px;height:20px;fill:var(--magenta)}

  .panel{position:absolute;left:431px;top:0;width:421px;height:487px;background:var(--grad);
    border-radius:92px 0 92px 0;color:var(--paper)}
  .services{position:absolute;left:0;right:0;top:68px;text-align:center;list-style:none;
    font-family:"Montserrat",sans-serif;font-weight:600;font-size:20px;line-height:28.5px;letter-spacing:.5px;padding-left:30px}
  .services li::before{content:"";display:inline-block;width:12px;height:12px;border-radius:2px;background:var(--paper);margin-right:8px;vertical-align:1px}
  .address{position:absolute;left:38px;top:210px;font-size:18.5px;line-height:29px}
  .contacts{position:absolute;left:38px;top:311px;font-size:18.5px;line-height:29px;white-space:nowrap}
  .contacts b{font-weight:700}

  .hotline{position:absolute;left:188px;top:415px;width:436px;height:52px;background:var(--paper);
    border-radius:0 30px 30px 0;display:flex;align-items:center;gap:16px;z-index:2}
  .hotline__icon{width:45px;height:46px;border-radius:8px;background:var(--ink);display:flex;align-items:center;justify-content:center;flex:none}
  .hotline__icon svg{width:28px;height:28px;fill:var(--paper)}
  .hotline__number{font-family:"Montserrat",sans-serif;font-weight:700;font-size:41px;letter-spacing:3px;color:var(--ink);white-space:nowrap}

  /* front side */
  .front-brand{position:absolute;left:0;right:0;top:198px;display:flex;justify-content:center;align-items:center;gap:18px;
    font-family:"Montserrat",sans-serif;font-weight:700;font-size:72px;letter-spacing:-.5px;color:var(--paper)}
  .front-brand__mark{width:30px;height:30px;background:var(--paper)}
  .front-band{position:absolute;left:0;right:0;top:360px;height:79px;background:var(--paper);
    display:flex;align-items:center;justify-content:center;gap:18px}
  .front-band .hotline__icon{width:49px;height:49px}
  .front-band .hotline__number{font-size:46px;letter-spacing:4px}
</style>
</head>
<body>

<section class="card card--info" aria-label="Business card, contact side">
  <div class="brand"><span class="brand__mark"></span>Beacon Cabs</div>

  <div class="line-list">
    <div class="line"><span class="line__icon"><svg viewBox="0 0 24 24"><path d="M6.6 10.8c1.4 2.8 3.8 5.1 6.6 6.6l2.2-2.2c.3-.3.7-.4 1-.2 1.1.4 2.3.6 3.6.6.6 0 1 .4 1 1V20c0 .6-.4 1-1 1C10.6 21 3 13.4 3 4c0-.6.4-1 1-1h3.5c.6 0 1 .4 1 1 0 1.3.2 2.5.6 3.6.1.3 0 .7-.2 1z"/></svg></span>01632 41 52 52</div>
    <div class="line"><span class="line__icon"><svg viewBox="0 0 24 24"><path d="M6.6 10.8c1.4 2.8 3.8 5.1 6.6 6.6l2.2-2.2c.3-.3.7-.4 1-.2 1.1.4 2.3.6 3.6.6.6 0 1 .4 1 1V20c0 .6-.4 1-1 1C10.6 21 3 13.4 3 4c0-.6.4-1 1-1h3.5c.6 0 1 .4 1 1 0 1.3.2 2.5.6 3.6.1.3 0 .7-.2 1z"/></svg></span>01632 63 63 63</div>
    <div class="line"><span class="line__icon"><svg viewBox="0 0 24 24"><path d="M6.6 10.8c1.4 2.8 3.8 5.1 6.6 6.6l2.2-2.2c.3-.3.7-.4 1-.2 1.1.4 2.3.6 3.6.6.6 0 1 .4 1 1V20c0 .6-.4 1-1 1C10.6 21 3 13.4 3 4c0-.6.4-1 1-1h3.5c.6 0 1 .4 1 1 0 1.3.2 2.5.6 3.6.1.3 0 .7-.2 1z"/></svg></span>01632 57 94 22</div>
  </div>

  <div class="panel">
    <ul class="services">
      <li>AIRPORT TRANSFERS</li>
      <li>MINIBUSES</li>
      <li>SCHOOL TRANSPORT</li>
    </ul>
    <p class="address">St Marys Parish Hall<br>Market Row<br>Bramford, BR4 1XY</p>
    <p class="contacts">
      <b>Freephone:</b> 0800 000 0 111<br>
      <b>Email:</b> beaconcabs@mailbox.co.uk<br>
      <b>Website:</b> www.bramfordcabs.co.uk
    </p>
  </div>

  <div class="hotline">
    <span class="hotline__icon"><svg viewBox="0 0 24 24"><path d="M6.6 10.8c1.4 2.8 3.8 5.1 6.6 6.6l2.2-2.2c.3-.3.7-.4 1-.2 1.1.4 2.3.6 3.6.6.6 0 1 .4 1 1V20c0 .6-.4 1-1 1C10.6 21 3 13.4 3 4c0-.6.4-1 1-1h3.5c.6 0 1 .4 1 1 0 1.3.2 2.5.6 3.6.1.3 0 .7-.2 1z"/></svg></span>
    <span class="hotline__number">01632 480 480</span>
  </div>
</section>

<section class="card card--front" aria-label="Business card, front side">
  <div class="front-brand"><span class="front-brand__mark"></span>Beacon Cabs</div>
  <div class="front-band">
    <span class="hotline__icon"><svg viewBox="0 0 24 24"><path d="M6.6 10.8c1.4 2.8 3.8 5.1 6.6 6.6l2.2-2.2c.3-.3.7-.4 1-.2 1.1.4 2.3.6 3.6.6.6 0 1 .4 1 1V20c0 .6-.4 1-1 1C10.6 21 3 13.4 3 4c0-.6.4-1 1-1h3.5c.6 0 1 .4 1 1 0 1.3.2 2.5.6 3.6.1.3 0 .7-.2 1z"/></svg></span>
    <span class="hotline__number">01632 480 480</span>
  </div>
</section>

</body>
</html>
```